Interior Decoration and Concept Store needs a webpage design

Sophisticated website for my business, name Wren Hollow. Wren Hollow is a design service and homewares store run by interior decorator Marion Tulk.

Marion's qualification and work experience as an interior decorator, is able to provide advice and recommendations for interior and exterior concepts, colour consultations, furniture, lighting, decor concepts and products are sourced for individual projects. A re-upholstery service is also provided.

plain circle icon.
Projects page.
Profile page.
Established 2009
Medial page

Industry/Entity Type

Store

```html
<!DOCTYPE html>
<html lang="en">
<head>
<meta charset="utf-8">
<title>Wren Hollow — Interior Decoration</title>
<link rel="stylesheet" href="https://fonts.googleapis.com/css2?family=Raleway:wght@200;300&display=swap">
<style>
  :root {
    --ink: #333333;
    --ink-soft: #555555;
    --muted: #777777;
    --rule: #9a9a9a;
    --icon: #6e6e6e;
    --paper: #ffffff;
    --label: #ffffff;
  }
  * { box-sizing: border-box; margin: 0; padding: 0; }
  html, body { width: 966px; height: 1200px; overflow: hidden; background: var(--paper); }
  body { font-family: "Raleway", sans-serif; color: var(--ink); position: relative; }

  .brand-header { height: 160px; display: flex; align-items: center; justify-content: center; }
  .brand-name { font-family: "Raleway", sans-serif; font-weight: 200; font-size: 58px; letter-spacing: 2px; color: var(--ink); }

  .main-nav { height: 52px; display: flex; align-items: center; justify-content: space-between; padding: 0 38px 0 48px; }
  .main-nav a { font-weight: 300; font-size: 21px; color: var(--ink); text-decoration: none; }
  .main-nav .divider { width: 1px; height: 31px; background: var(--ink); }

  .service-grid { position: absolute; top: 213px; left: 0; width: 966px; height: 724px;
    display: grid; grid-template-columns: repeat(4, 1fr); grid-template-rows: repeat(2, 1fr); }
  .tile { position: relative; display: flex; align-items: center; justify-content: center; }
  .tile-label { font-weight: 300; font-size: 26px; line-height: 30px; color: var(--label); text-align: center; }
  .tile--bedroom { background: linear-gradient(160deg, #e6e2dc 0%, #cfc8bf 50%, #8c8279 100%); }
  .tile--dining { background: linear-gradient(170deg, #8b8b8d 0%, #6f6d6d 60%, #5a5552 100%); }
  .tile--living { background: linear-gradient(170deg, #f2f0ec 0%, #e8e2d8 50%, #c9b78a 100%); }
  .tile--lighting { background: linear-gradient(170deg, #8f8f8c 0%, #858079 55%, #77716b 100%); }
  .tile--colour { background: linear-gradient(170deg, #8d8a86 0%, #848482 60%, #7b7b7b 100%); }
  .tile--lounge { background: linear-gradient(180deg, #f4f2ef 0%, #eae6e0 55%, #2a9a9c 75%, #9a5a2e 100%); }
  .tile--furniture { background: linear-gradient(170deg, #6f6f71 0%, #858382 55%, #8e8a87 100%); }
  .tile--kitchen { background: linear-gradient(175deg, #f3f2ef 0%, #e7e4df 55%, #6f6a2a 78%, #4a3a32 100%); }

  .site-footer { position: absolute; top: 970px; left: 0; width: 966px; height: 170px; }
  .footer-about { position: absolute; left: 30px; top: 10px; width: 250px; }
  .footer-about .brand-name { font-size: 34px; letter-spacing: 1px; display: block; margin-bottom: 30px; }
  .footer-about p { font-family: Arial, sans-serif; font-size: 12px; line-height: 16px; color: var(--ink-soft); }

  .footer-heading { font-weight: 200; font-size: 35px; letter-spacing: -1px; color: var(--ink); line-height: 40px; }
  .footer-social { position: absolute; left: 340px; top: 12px; }
  .social-list { display: flex; gap: 14px; margin-top: 17px; list-style: none; }
  .social-list li { width: 43px; height: 43px; border-radius: 50%; background: var(--icon); }

  .footer-contact { position: absolute; left: 680px; top: 12px; font-family: Arial, sans-serif; color: var(--ink-soft); }
  .footer-contact .footer-heading { font-family: "Raleway", sans-serif; margin-bottom: 12px; }
  .contact-name { font-size: 14px; margin-left: 3px; }
  .contact-address { font-size: 12px; line-height: 18px; margin: 2px 0 0 3px; font-style: normal; }
  .contact-phone { display: flex; align-items: center; gap: 6px; font-size: 23px; color: var(--muted); margin-top: 6px; }
  .contact-email { font-size: 14px; margin: 6px 0 0 3px; }

  .footer-rule { position: absolute; top: 1154px; left: 0; width: 966px; height: 1px; background: var(--rule); }
  .footer-bar { position: absolute; top: 1171px; left: 0; width: 966px; display: flex; justify-content: space-between; padding: 0 30px 0 26px;
    font-family: Arial, sans-serif; font-size: 11px; color: var(--ink); }
  .footer-nav { display: flex; gap: 0; }
  .footer-nav a { color: var(--ink); text-decoration: none; width: 84px; }
  .footer-nav a:nth-child(4) { width: 110px; }
</style>
</head>
<body>
  <header class="brand-header">
    <span class="brand-name">Wren Hollow</span>
  </header>

  <nav class="main-nav">
    <a href="#">home</a><span class="divider"></span>
    <a href="#">about</a><span class="divider"></span>
    <a href="#">projects</a><span class="divider"></span>
    <a href="#">testimonials</a><span class="divider"></span>
    <a href="#">awards</a><span class="divider"></span>
    <a href="#">contact us</a>
  </nav>

  <main class="service-grid">
    <div class="tile tile--bedroom" role="img" aria-label="Photo of a bright bedroom with a woven pendant, bedside lamp and grey throw"></div>
    <div class="tile tile--dining" role="img" aria-label="Photo of a dining area with wall clock and dark chairs, grey tinted"><span class="tile-label">decore<br>concepts</span></div>
    <div class="tile tile--living" role="img" aria-label="Photo of a living room with timber shelving, desk and patterned cushions"></div>
    <div class="tile tile--lighting" role="img" aria-label="Photo of a curved side table with a lamp by a glass door, grey tinted"><span class="tile-label">lightning</span></div>
    <div class="tile tile--colour" role="img" aria-label="Photo of a room with an abstract colourful painting, grey tinted"><span class="tile-label">colour<br>consultations</span></div>
    <div class="tile tile--lounge" role="img" aria-label="Photo of a lounge with teal chest of drawers, framed art, fireplace and patterned rug"></div>
    <div class="tile tile--furniture" role="img" aria-label="Photo of an armchair and ottoman by a glass door, grey tinted"><span class="tile-label">furnitures</span></div>
    <div class="tile tile--kitchen" role="img" aria-label="Photo of a kitchen bench with stools, red vases, art print and olive armchair"></div>
  </main>

  <footer>
    <div class="site-footer">
      <div class="footer-about">
        <span class="brand-name">Wren Hollow</span>
        <p>Sed ut perspiciatis, unde omnis iste natus error sit voluptatem accusantium doloremque laudantium, totam rem aperiam eaque ipsa.</p>
      </div>

      <div class="footer-social">
        <h2 class="footer-heading">CONNECT WITH US</h2>
        <ul class="social-list">
          <li aria-label="Social link"></li>
          <li aria-label="Social link"></li>
          <li aria-label="Social link"></li>
          <li aria-label="Social link"></li>
          <li aria-label="Social link"></li>
        </ul>
      </div>

      <div class="footer-contact">
        <h2 class="footer-heading">CONTACT US</h2>
        <div class="contact-name">Wren Hollow</div>
        <address class="contact-address">88 Alder Lane Studio 4<br>Marsh End, Fernvale 240117</address>
        <div class="contact-phone">
          <svg width="28" height="28" viewBox="0 0 28 28" aria-hidden="true">
            <circle cx="14" cy="14" r="12.5" fill="none" stroke="#777" stroke-width="1.6"/>
            <path d="M10 7.5c1-.6 1.8-.4 2.2.4l1 2.2c.3.7.1 1.3-.5 1.7l-.8.5c.5 1.6 1.6 3.1 3 4.1l.7-.6c.6-.5 1.2-.5 1.8-.1l2 1.3c.7.5.8 1.3.2 2.1-1 1.4-2.4 1.8-4 1-3.4-1.7-5.8-4.8-6.6-8.6-.3-1.6.3-3.2 1-4z" fill="#777"/>
          </svg>
          <span>014.552.0938</span>
        </div>
        <div class="contact-email">hello@wrenhollow.com</div>
      </div>
    </div>

    <div class="footer-rule"></div>

    <div class="footer-bar">
      <nav class="footer-nav">
        <a href="#">home</a>
        <a href="#">about</a>
        <a href="#">projects</a>
        <a href="#">testimonials</a>
        <a href="#">awards</a>
        <a href="#">contact us</a>
      </nav>
      <span>© Copyright Wren Hollow 2014. All Rights Reserved</span>
    </div>
  </footer>
</body>
</html>
```